We need a company profile design 8 + cover

The company profile is attached below, we need to renew the whole thing with full modification. content and page arrangement is the same. All should be A5 size printable and electronic copies.

I attached logo and colors for identity, please use logo colors as main scheme colours

We need 2 copies Arabic and English

Font styles to use
Sans Serif

Requirements
Nice to have
• Please let us know how we can use the designs to edit in Arabic

```html
<!DOCTYPE html>
<html lang="en">
<head>
<meta charset="utf-8">
<title>Nova Scholar – Company Profile Cover</title>
<link href="https://fonts.googleapis.com/css2?family=Archivo+Black&family=Arimo:wght@400;700&display=swap" rel="stylesheet">
<style>
  :root {
    --navy: #15276a;
    --paper: #f3f3f4;
    --backdrop: #9c9a9a;
    --ink: #1b1f33;
    --photo-warm-a: #f1d9b0;
    --photo-warm-b: #e0a33a;
    --photo-dark-a: #6b5a4e;
    --photo-dark-b: #2a2522;
  }
  * { box-sizing: border-box; margin: 0; padding: 0; }
  html, body { width: 1200px; height: 1200px; overflow: hidden; }
  body { background: var(--backdrop); font-family: "Arimo", Arial, sans-serif; }

  .spread {
    position: absolute; left: 100px; top: 246px;
    width: 1000px; height: 707px;
    display: flex;
    box-shadow: 0 10px 30px rgba(0,0,0,.25);
  }
  .page { position: relative; width: 500px; height: 707px; background: var(--paper); overflow: hidden; }
  .page svg.shapes { position: absolute; inset: 0; }

  .slogan {
    position: absolute; right: 30px; top: 150px; text-align: right;
    font-family: "Archivo Black", "Arial Black", sans-serif;
    color: var(--navy); font-size: 30px; line-height: 1.02; letter-spacing: 1px;
  }

  .contact-list { position: absolute; left: 40px; top: 440px; list-style: none; }
  .contact-list li {
    display: flex; align-items: flex-start; gap: 14px;
    font-size: 13px; line-height: 1.3; color: var(--ink); margin-bottom: 9px;
  }
  .contact-icon {
    flex: none; width: 20px; height: 20px; border-radius: 50%;
    background: var(--navy); display: flex; align-items: center; justify-content: center;
  }
  .contact-icon svg { width: 12px; height: 12px; }

  .brand {
    position: absolute; right: 24px; top: 170px;
    padding: 12px 16px; background: var(--paper);
    text-align: center; white-space: nowrap;
    font-family: "Archivo Black", "Arial Black", sans-serif;
    color: var(--navy); font-size: 24px; line-height: 1.05;
  }

  .service-title {
    position: absolute; left: 40px; top: 585px;
    font-family: "Archivo Black", "Arial Black", sans-serif;
    color: var(--navy); font-size: 28px; line-height: 1.1; letter-spacing: .5px;
    white-space: nowrap;
  }
  .service-url {
    position: absolute; left: 120px; top: 668px;
    font-family: "Arimo", Arial, sans-serif; font-weight: 700;
    color: var(--ink); font-size: 13px; letter-spacing: 1px;
  }
</style>
</head>
<body>
<main class="spread">

  <section class="page back-cover">
    <svg class="shapes" viewBox="0 0 500 707" width="500" height="707">
      <defs>
        <linearGradient id="warmPhoto" x1="0" y1="0" x2="1" y2="1">
          <stop offset="0" stop-color="var(--photo-warm-a)"/>
          <stop offset=".55" stop-color="var(--photo-warm-b)"/>
          <stop offset="1" stop-color="#f6e6cc"/>
        </linearGradient>
      </defs>
      <path d="M0 0 H500 V350 Q260 420 0 320 Z" fill="url(#warmPhoto)"
            role="img" aria-label="Photo of a smiling student with a backpack giving a thumbs up on campus"/>
      <path d="M0 320 Q260 420 500 350 V370 Q260 438 0 336 Z" fill="var(--navy)"/>
    </svg>
    <div class="slogan">BE<br>AMONG<br>THE BEST</div>

    <ul class="contact-list">
      <li><span class="contact-icon"><svg viewBox="0 0 12 12"><path d="M6 1a3.5 3.5 0 0 0-3.5 3.5C2.5 7 6 11 6 11s3.5-4 3.5-6.5A3.5 3.5 0 0 0 6 1Zm0 4.8a1.3 1.3 0 1 1 0-2.6 1.3 1.3 0 0 1 0 2.6Z" fill="#fff"/></svg></span>
        <span>Harbour View Tower / Marina District<br>Suite 12, 4th Floor, PO Box - 4820</span></li>
      <li><span class="contact-icon"><svg viewBox="0 0 12 12"><path d="M3 1.5 4.6 1l1 2.4-1 .8a6 6 0 0 0 2.8 2.8l.8-1 2.4 1-.5 1.6C9.6 9.3 9 9.6 8.4 9.5 5.3 8.9 2.9 6.5 2.3 3.4c-.1-.6.2-1.2.7-1.9Z" fill="#fff"/></svg></span>
        <span>+971 2 555 01 23 | +971 50 555 0147<br>+971 52 555 0199 | +971 505550162</span></li>
      <li><span class="contact-icon"><svg viewBox="0 0 12 12"><rect x="1.5" y="3" width="9" height="6" fill="none" stroke="#fff" stroke-width="1.1"/><path d="M1.5 3 6 6.5 10.5 3" fill="none" stroke="#fff" stroke-width="1.1"/></svg></span>
        <span>info@novascholar.example</span></li>
      <li><span class="contact-icon"><svg viewBox="0 0 12 12"><circle cx="6" cy="6" r="4.3" fill="none" stroke="#fff" stroke-width="1"/><ellipse cx="6" cy="6" rx="1.9" ry="4.3" fill="none" stroke="#fff" stroke-width="1"/><path d="M1.7 6h8.6" stroke="#fff" stroke-width="1"/></svg></span>
        <span>www.novascholar.example</span></li>
      <li><span class="contact-icon"></span><span>Facebook.com/NOVA-SCHOLAR</span></li>
      <li><span class="contact-icon"></span><span>Twitter.com/novascholar_hq</span></li>
      <li><span class="contact-icon"></span><span>novascholar.hq</span></li>
    </ul>
  </section>

  <section class="page front-cover">
    <svg class="shapes" viewBox="0 0 500 707" width="500" height="707">
      <defs>
        <linearGradient id="groupPhoto" x1="0" y1="0" x2="1" y2="1">
          <stop offset="0" stop-color="#efe7dc"/>
          <stop offset=".3" stop-color="var(--photo-dark-a)"/>
          <stop offset="1" stop-color="var(--photo-dark-b)"/>
        </linearGradient>
      </defs>
      <path d="M0 320 L0 350 L40 430 L500 560 V544 L52 414 L14 340 Z" fill="var(--navy)"/>
      <path d="M60 0 H500 V528 L58 402 L24 336 Z" fill="url(#groupPhoto)"
            role="img" aria-label="Group photo of smiling university students sitting together on a staircase"/>
    </svg>
    <div class="brand">NOVA<br>SCHOLAR</div>
    <h1 class="service-title">ACADEMIC AND STUDY<br>ABROAD SERVICES</h1>
    <p class="service-url">WWW.NOVASCHOLAR.EXAMPLE</p>
  </section>

</main>
</body>
</html>
```